Welcome to the neighborhood Flyer

We want to create a postcard that welcomes our customers to the neighborhood. We want the front of the postcard to say "Welcome to the neighborhood" and have our store info:
Bramble 27 Wine & Spirits
412 Orchard Ln (19th Street)
(555) 204-7381
www.bramble27vino.example
Free neighborhood deliveries

On the back of the postcard we want to let our customers know of our Daily Specials.
Daily Specials 10% off at Bramble 27
Magnum Mondays : All 1.5L Wines
Tuscan Tuesdays : All 750ml Italian Wines
Wine-in-a-Box Wednesdays : All boxed Wines
Thirsty Thursdays : All 750ml Sparkling/Champagne
French Fridays : All 750ml French Wines
Surfin' Saturdays : All 750ml Californian Wines
South American & Spanish Sundays : All 750ml
We are thinking of black and white for both sides but we are open to any ideas and suggestions on color and wording!Thanks

Requirements
Must have
• Store info
Nice to have
• A Clean layout
• Nice and simple
Should not have
• Overcrowded wording

```html
<!DOCTYPE html>
<html lang="en">
<head>
<meta charset="utf-8">
<title>Bramble 27 Wine &amp; Spirits – Welcome Postcard</title>
<link rel="stylesheet" href="https://fonts.googleapis.com/css2?family=Bebas+Neue&family=Oswald:wght@400;500&family=Roboto:wght@400;500;700&display=swap">
<style>
  :root {
    --page: #ececec;
    --ink: #1b1b1b;
    --panel: #231f20;
    --row: #3a3a3a;
    --red: #e31e24;
    --white: #ffffff;
    --grey-text: #555555;
    --line: #c9c9c9;
    --muted: #bdbdbd;
  }
  * { margin: 0; padding: 0; box-sizing: border-box; }
  html, body { width: 1000px; height: 1200px; overflow: hidden; }
  body {
    background: var(--page);
    position: relative;
    font-family: "Roboto", Arial, sans-serif;
  }

  /* ---------- Front of card ---------- */
  .card-front {
    position: absolute; left: 110px; top: 20px;
    width: 716px; height: 587px;
    background: var(--ink);
    overflow: hidden;
  }
  .storefront-photo {
    position: absolute; left: 0; top: 0; width: 716px; height: 534px;
    background:
      linear-gradient(180deg, #2a2a2a 0%, #3c3c3c 14%, #161616 20%, #5a5a5a 45%, #8d8d8d 62%, #b9b9b9 78%, #9a9a9a 100%);
  }
  .store-sign {
    position: absolute; left: 0; top: 48px; width: 716px;
    text-align: center;
    font-family: "Oswald", Arial, sans-serif; font-weight: 500;
    font-size: 44px; letter-spacing: 2px; color: var(--white);
  }
  .headline {
    position: absolute; left: 200px; top: 214px; width: 330px;
    text-align: center; color: var(--red);
    font-family: "Bebas Neue", Impact, sans-serif;
    font-weight: 400;
  }
  .headline-welcome { font-size: 96px; line-height: 86px; display: block; }
  .headline-to-the {
    display: flex; align-items: center; justify-content: center; gap: 10px;
    font-size: 26px; line-height: 30px; margin-top: 4px;
  }
  .headline-to-the::before, .headline-to-the::after {
    content: ""; width: 80px; height: 2px; background: var(--ink);
  }
  .headline-neighborhood { display: block; font-size: 52px; line-height: 50px; margin-top: 2px; }
  .front-banner { position: absolute; left: 0; top: 0; }
  .store-info-bar {
    position: absolute; left: 0; top: 534px; width: 716px; height: 53px;
    background: var(--ink); color: var(--white);
    display: flex; align-items: center; justify-content: space-between;
    padding: 0 22px; font-size: 12px;
  }
  .info-item { display: flex; align-items: center; gap: 7px; white-space: nowrap; }
  .info-item svg { flex: none; }

  /* ---------- Back of card ---------- */
  .card-back {
    position: absolute; left: 174px; top: 627px;
    width: 716px; height: 553px;
    background: var(--white);
  }
  .specials-panel {
    position: absolute; left: 0; top: 0; width: 362px; height: 553px;
    background: var(--panel); color: var(--white);
  }
  .panel-brand {
    position: absolute; left: 0; top: 22px; width: 362px; text-align: center;
    font-family: "Oswald", Arial, sans-serif; font-weight: 400;
    font-size: 30px; line-height: 40px; color: var(--white);
  }
  .panel-title {
    position: absolute; left: 0; top: 74px; width: 362px; text-align: center;
    font-family: "Oswald", Arial, sans-serif; font-weight: 400;
    font-size: 24px; line-height: 30px;
  }
  .panel-banner { position: absolute; left: 0; top: 0; }
  .store-interior-photo {
    position: absolute; left: 0; top: 143px; width: 362px; height: 145px;
    background: linear-gradient(180deg, #d8d8d8 0%, #9c9c9c 40%, #555 75%, #3a3a3a 100%);
  }
  .specials-heading {
    position: absolute; left: 0; top: 298px; width: 362px; text-align: center;
    font-size: 12px; line-height: 15px; color: var(--white);
  }
  .specials-list {
    position: absolute; left: 16px; top: 340px; width: 330px;
    list-style: none;
  }
  .special-row {
    display: flex; align-items: center; height: 20px; margin-bottom: 3.6px;
    font-size: 10.5px;
  }
  .special-row:nth-child(odd) { background: var(--row); }
  .special-day {
    width: 76px; padding-left: 4px;
    font-size: 8px; letter-spacing: 0.3px; color: var(--muted);
  }
  .special-item { color: var(--white); }
  .panel-url {
    position: absolute; left: 0; top: 516px; width: 362px; text-align: center;
    color: var(--red); font-size: 14px; font-weight: 500;
  }

  .mailing-side { position: absolute; left: 362px; top: 0; width: 354px; height: 553px; }
  .return-address { position: absolute; left: 26px; top: 20px; color: var(--grey-text); }
  .return-name { font-size: 14px; color: #333; line-height: 20px; }
  .return-line { font-size: 11px; font-weight: 500; line-height: 15px; }
  .stamp-box {
    position: absolute; left: 247px; top: 26px; width: 86px; height: 54px;
    border: 1px solid var(--line);
  }
  .address-lines { position: absolute; left: 38px; top: 211px; width: 293px; }
  .address-line { height: 36.3px; border-top: 1px solid var(--line); }
</style>
</head>
<body>

<section class="card-front" aria-label="Postcard front">
  <div class="storefront-photo" role="img" aria-label="Black and white photo of the shop front at night with lit display windows and passers-by on the sidewalk"></div>
  <div class="store-sign">BRAMBLE 27 WINE &amp; SPIRITS</div>

  <h1 class="headline">
    <span class="headline-welcome">WELCOME</span>
    <span class="headline-to-the">TO THE</span>
    <span class="headline-neighborhood">NEIGHBORHOOD</span>
  </h1>

  <svg class="front-banner" width="716" height="534" viewBox="0 0 716 534">
    <path d="M94,389 C250,405 420,414 573,402 L556,470 L533,446 L516,522 L504,463 C430,470 350,470 300,462 C230,450 160,424 94,389 Z" fill="#ffffff"/>
    <text x="424" y="450" text-anchor="middle" transform="rotate(4 424 450)"
          font-family="Roboto, Arial, sans-serif" font-weight="700" font-size="15" fill="#1b1b1b">FREE NEIGHBORHOOD DELIVERIES</text>
  </svg>

  <footer class="store-info-bar">
    <span class="info-item">
      <svg width="14" height="16" viewBox="0 0 14 16"><path d="M7 1a5 5 0 0 0-5 5c0 4 5 9 5 9s5-5 5-9a5 5 0 0 0-5-5z" fill="none" stroke="#fff" stroke-width="1.4"/><circle cx="7" cy="6" r="1.8" fill="#fff"/></svg>
      Bramble 27 Wine &amp; Spirits 412 Orchard Ln (19th Street)
    </span>
    <span class="info-item">
      <svg width="15" height="15" viewBox="0 0 16 16"><circle cx="8" cy="8" r="7" fill="none" stroke="#fff" stroke-width="1.3"/><path d="M5.5 4.5l1.5 0 .7 2-1 .8a5 5 0 0 0 2 2l.8-1 2 .7v1.5c-3 .5-6.5-3-6-6z" fill="#fff"/></svg>
      (555) 204-7381
    </span>
    <span class="info-item">
      <svg width="15" height="15" viewBox="0 0 16 16"><circle cx="8" cy="8" r="7" fill="none" stroke="#fff" stroke-width="1.3"/><rect x="7.2" y="7" width="1.6" height="5" fill="#fff"/><circle cx="8" cy="4.8" r="1" fill="#fff"/></svg>
      www.bramble27vino.example
    </span>
  </footer>
</section>

<section class="card-back" aria-label="Postcard back">
  <div class="specials-panel">
    <div class="panel-brand">Bramble 27</div>
    <h2 class="panel-title">OUR DAILY SPECIALS</h2>
    <svg class="panel-banner" width="362" height="170" viewBox="0 0 362 170">
      <path d="M110,100 C170,108 240,110 292,100 L281,134 L268,127 L261,150 L255,136 C210,142 150,136 110,100 Z" fill="#ffffff"/>
      <text x="277" y="124" text-anchor="end" transform="rotate(3 277 124)"
            font-family="Roboto, Arial, sans-serif" font-weight="700" font-size="7.5" fill="#1b1b1b">FREE NEIGHBORHOOD DELIVERIES</text>
    </svg>
    <div class="store-interior-photo" role="img" aria-label="Black and white photo of the shop interior with wine racks and shelves"></div>

    <p class="specials-heading">DAILY SPECIALS<br>10% off at Bramble 27</p>

    <ul class="specials-list">
      <li class="special-row"><span class="special-day">MONDAYS</span><span class="special-item">All 1.5L Wines</span></li>
      <li class="special-row"><span class="special-day">TUESDAYS</span><span class="special-item">All 750ml Italian Wines</span></li>
      <li class="special-row"><span class="special-day">WEDNESDAYS</span><span class="special-item">All boxed Wines</span></li>
      <li class="special-row"><span class="special-day">THURSDAYS</span><span class="special-item">All 750ml Sparkling/Champagne</span></li>
      <li class="special-row"><span class="special-day">FRIDAYS</span><span class="special-item">All 750ml French Wines</span></li>
      <li class="special-row"><span class="special-day">SATURDAYS</span><span class="special-item">All 750ml Californian Wines</span></li>
      <li class="special-row"><span class="special-day">SUNDAYS</span><span class="special-item">All 750ml</span></li>
    </ul>

    <div class="panel-url">www.bramble27vino.example</div>
  </div>

  <div class="mailing-side">
    <div class="return-address">
      <div class="return-name">Bramble 27</div>
      <div class="return-line">Bramble 27 Wine &amp; Spirits 412</div>
      <div class="return-line">Orchard Ln (19th Street)</div>
    </div>
    <div class="stamp-box"></div>
    <div class="address-lines">
      <div class="address-line"></div>
      <div class="address-line"></div>
      <div class="address-line"></div>
      <div class="address-line"></div>
      <div class="address-line"></div>
    </div>
  </div>
</section>

</body>
</html>
```